Adept Corvana Recruitment company

We require a website for job recruitment company called "Adept Corvana"
Our company is specialising in recruitment of skilled labour from Sri Lanka into Australian market.
We would like to include a job advertising plugin where jobs can be listed and applied for .
COPYWRITING MUST BE INCLUDED !

Industry/Entity Type

Recruitment

Coding

Coded - Design and coding required

Number of Pages Required

5+ page

Colors

Designer to choose colors to be used in the design.

```html
<!DOCTYPE html>
<html lang="en">
<head>
<meta charset="utf-8">
<title>Adept Corvana Recruitment</title>
<link href="https://fonts.googleapis.com/css2?family=Montserrat:wght@500;600;700&family=Lato:wght@400;700&display=swap" rel="stylesheet">
<style>
:root{
  --blue:#0d55a3;
  --navy:#0a3c85;
  --deep:#15277a;
  --teal:#5cc6c9;
  --green:#2a9d8f;
  --ink:#111;
  --text:#222;
  --grey:#6b6b6b;
  --panel:#e9f0f8;
  --row:#e5edf7;
  --footer:#5b5b5c;
  --white:#fff;
}
*{margin:0;padding:0;box-sizing:border-box}
html,body{width:1200px;height:4777px;overflow:hidden}
body{position:relative;background:var(--white);font-family:"Lato",sans-serif;color:var(--text)}
.abs{position:absolute}
.h-font{font-family:"Montserrat",sans-serif}
.btn{position:absolute;display:flex;align-items:center;justify-content:center;background:var(--ink);color:var(--white);border-radius:40px;font-family:"Montserrat",sans-serif;font-weight:600;font-size:17px}
.eyebrow{font-family:"Montserrat",sans-serif;color:var(--blue);font-weight:500;font-size:22px}
.title{font-family:"Montserrat",sans-serif;font-weight:600;color:var(--ink);font-size:35px}
.center{left:0;width:1200px;text-align:center}

/* header */
.site-header{position:absolute;top:0;left:0;width:1200px;height:126px;background:var(--white)}
.brand{position:absolute;font-family:"Montserrat",sans-serif;font-weight:700;color:#4a4a4a;font-size:40px;line-height:1}
.nav{position:absolute;left:488px;top:84px;display:flex;gap:21px;font-family:"Montserrat",sans-serif;font-size:16px;font-weight:500;color:var(--ink)}
.nav .active{color:var(--blue)}
.login{position:absolute;left:773px;top:18px;width:72px;height:40px;border:1.5px solid var(--ink);border-radius:24px;display:flex;align-items:center;justify-content:center;font-size:14px;font-family:"Montserrat",sans-serif;gap:4px}
.join{position:absolute;left:885px;top:18px;width:204px;height:40px;background:var(--ink);color:var(--white);border-radius:24px;display:flex;align-items:center;justify-content:center;font-size:14px;font-family:"Montserrat",sans-serif;font-weight:600}

/* hero */
.hero{position:absolute;top:126px;left:0;width:1200px;height:581px;background:var(--blue);overflow:hidden}
.hero-photo{position:absolute;inset:0;background:linear-gradient(120deg,#e7e5e2 0%,#cfcac4 45%,#8f8a85 100%);clip-path:polygon(452px 0,1200px 0,1200px 581px,655px 581px)}
.hero h1{position:absolute;left:108px;top:90px;font-family:"Montserrat",sans-serif;font-weight:700;color:var(--white);font-size:46px;line-height:50px}
.hero label{position:absolute;left:111px;color:var(--white);font-family:"Montserrat",sans-serif;font-size:20px;font-weight:500}
.field{position:absolute;left:111px;width:382px;height:54px;background:var(--white);border-radius:3px;padding-left:16px;display:flex;align-items:center;font-size:16px;color:#555}

/* audiences */
.audience{position:absolute;top:728px;left:17px;width:1166px;height:434px;background:var(--panel)}
.figure{position:absolute;left:492px;top:0;width:182px;height:434px;background:linear-gradient(#f6f9fc,#fbfcfe)}
.aud-col{position:absolute;top:44px;width:450px}
.aud-col .eyebrow{font-size:22px}
.aud-col h2{font-family:"Montserrat",sans-serif;font-weight:600;font-size:33px;color:var(--ink);margin-top:14px}
.aud-col p{margin-top:20px;font-size:15.5px;line-height:27px;color:var(--grey)}

/* welcome */
.welcome p{font-family:"Montserrat",sans-serif;font-size:25px;line-height:36px;color:#666}

/* process */
.process{position:absolute;top:1617px;left:0;width:1200px;height:636px;background:var(--panel);overflow:hidden}
.step{position:absolute;font-family:"Montserrat",sans-serif;font-size:16px;line-height:22px;color:#222}
.step.r{text-align:right}

/* jobs */
.job-head{position:absolute;top:2446px;font-family:"Montserrat",sans-serif;font-size:18px;color:var(--ink)}
.job-row{position:absolute;left:111px;width:977px;height:127px}
.job-row.shade{background:var(--row)}
.job-logo{position:absolute;left:22px;top:28px;width:70px;height:70px;border-radius:50%;background:#d9dbde}
.job-title{position:absolute;left:102px;top:42px;font-family:"Montserrat",sans-serif;font-size:20px;color:var(--ink)}
.job-org{position:absolute;left:102px;top:73px;font-size:15px;color:#666}
.job-type{position:absolute;left:636px;top:55px;font-size:16px;color:#555}
.job-loc{position:absolute;left:770px;top:44px;font-size:16px;line-height:28px;color:#4a6a92}

/* join */
.join-band{position:absolute;top:3155px;left:0;width:1200px;height:580px;background:var(--blue);overflow:hidden}
.join-photo{position:absolute;inset:0;background:linear-gradient(110deg,#1b5d8c 0%,#2d7aa6 40%,#6a8fa8 100%);clip-path:polygon(0 0,650px 0,560px 580px,0 580px)}

/* posts */
.post{position:absolute;top:3912px;width:308px}
.post-img{height:218px}
.post h3{margin-top:38px;font-family:"Montserrat",sans-serif;font-weight:600;font-size:18.5px;line-height:26px;color:#222}
.post .by{margin-top:16px;font-size:16px;color:#666;display:flex;align-items:center;gap:6px}
.post p{margin-top:16px;font-size:16px;line-height:27px;color:#777}

/* footer */
.site-footer{position:absolute;top:4410px;left:0;width:1200px;height:367px;background:var(--footer);color:var(--white)}
.foot-col{position:absolute;top:75px}
.foot-col h4{font-family:"Montserrat",sans-serif;font-weight:600;font-size:19px;margin-bottom:20px}
.foot-col li{list-style:none;font-size:16px;line-height:25px}
.social{position:absolute;top:4730px;width:40px;height:40px;border-radius:50%;border:1.5px solid #eee}
</style>
</head>
<body>

<header class="site-header">
  <div class="brand" style="left:111px;top:40px;">Adept Corvana</div>
  <div class="login"><svg width="11" height="12" viewBox="0 0 11 12"><circle cx="5.5" cy="3.5" r="3" fill="#111"/><path d="M0 12c0-4 2.5-5 5.5-5s5.5 1 5.5 5z" fill="#111"/></svg>LOGIN</div>
  <div class="join">JOIN ADEPT CORVANA</div>
  <nav class="nav">
    <span class="active">Home</span><span>About Us</span><span>Job Seekers</span><span>Employer</span><span>News &amp; Insights</span><span>Contact Us</span>
  </nav>
</header>

<section class="hero">
  <div class="hero-photo" role="img" aria-label="Person typing on a laptop showing a job listings page"></div>
  <svg class="abs" style="left:0;top:0" width="1200" height="581">
    <polygon points="0,65 92,118 0,180" fill="var(--teal)"/>
    <polygon points="35,528 108,560 60,581 30,581" fill="var(--deep)"/>
    <polygon points="380,520 560,470 585,500 430,581 390,581" fill="var(--navy)" opacity=".9"/>
    <polygon points="525,512 585,455 590,512" fill="var(--green)"/>
  </svg>
  <h1>Find your<br>dream job now</h1>
  <label style="top:222px">Search for</label>
  <div class="field" style="top:261px">job Title or keyword</div>
  <label style="top:329px">Where</label>
  <div class="field" style="top:367px">city, state or postcode</div>
  <div class="btn" style="left:111px;top:446px;width:167px;height:59px;font-size:17px">SEARCH JOB</div>
</section>

<section class="audience">
  <div class="figure" role="img" aria-label="Faint silhouette of a professional in a suit"></div>
  <div class="aud-col" style="left:65px">
    <div class="eyebrow">For Employees</div>
    <h2>Looking for a Job?</h2>
    <p>Our ability to match the right employee with the right employer has helped many candidates in making life changing move to Australia and to become <span style="color:#333">PERMANENT RESIDENT</span> of Australia.</p>
  </div>
  <div class="btn" style="left:68px;top:324px;width:200px;height:61px">SUBMIT RESUME</div>
  <div class="aud-col" style="left:694px;width:450px">
    <div class="eyebrow">For Employers</div>
    <h2>Looking for Employees?</h2>
    <p>We know, how difficult it is to get the skilled labour force to help with business growth and expansion . That is why we search, screen and select only the best suitable candidates with all documents ready to apply for visa which will dramatically save your time and money. <span style="color:#333">Call us today</span> and let us help you expand your business.</p>
  </div>
  <div class="btn" style="left:698px;top:324px;width:182px;height:61px">POST JOBS</div>
</section>

<section class="welcome">
  <div class="abs center eyebrow" style="top:1236px">Get to know us</div>
  <div class="abs center title" style="top:1276px">Welcome to Adept Corvana</div>
  <p class="abs" style="left:170px;width:860px;top:1342px;text-align:center">We are recruitment company with the focus on Sri Lanka/ Australia Market.We are searching for skilled labour / proffessionals with experience and skillset required and we connect these people with employers in Australia.</p>
  <div class="abs center h-font" style="top:1520px;font-size:16px;font-weight:500">LEARN MORE &gt;&gt;</div>
</section>

<section class="process">
  <div class="abs center eyebrow" style="top:56px">Our Process</div>
  <div class="abs center title" style="top:98px">How it Works</div>
  <svg class="abs" style="left:0;top:0" width="1200" height="636">
    <circle cx="600" cy="600" r="213" fill="none" stroke="#444" stroke-width="1.3" stroke-dasharray="5 4"/>
    <circle cx="600" cy="585" r="168" fill="#fff"/>
    <g stroke="#555" stroke-width="1.2">
      <line x1="349" y1="541" x2="389" y2="541"/>
      <line x1="393" y1="440" x2="425" y2="462"/>
      <line x1="488" y1="356" x2="508" y2="390"/>
      <line x1="601" y1="329" x2="601" y2="387"/>
      <line x1="713" y1="356" x2="693" y2="390"/>
      <line x1="808" y1="440" x2="776" y2="462"/>
      <line x1="852" y1="541" x2="812" y2="541"/>
    </g>
    <g fill="var(--blue)">
      <circle cx="302" cy="541" r="46"/>
      <circle cx="354" cy="409" r="46"/>
      <circle cx="462" cy="312" r="46"/>
      <circle cx="601" cy="281" r="46"/>
      <circle cx="738" cy="318" r="46"/>
      <circle cx="846" cy="409" r="46"/>
      <circle cx="900" cy="541" r="46"/>
    </g>
    <g fill="none" stroke="#fff" stroke-width="2" stroke-linecap="round" stroke-linejoin="round">
      <!-- advertise -->
      <rect x="282" y="527" width="34" height="26" rx="2"/><line x1="316" y1="532" x2="322" y2="532"/><path d="M322 532v18a3 3 0 0 1-6 0"/><line x1="288" y1="545" x2="310" y2="545"/>
      <!-- collect -->
      <rect x="340" y="390" width="24" height="32" rx="2"/><rect x="346" y="396" width="24" height="32" rx="2"/><line x1="351" y1="405" x2="365" y2="405"/><line x1="351" y1="412" x2="365" y2="412"/><line x1="351" y1="419" x2="361" y2="419"/>
      <!-- review -->
      <circle cx="458" cy="301" r="6"/><path d="M446 322c0-8 5-12 12-12s12 4 12 12"/><path d="M470 300l8-8"/><circle cx="472" cy="296" r="8"/>
      <!-- shortlist -->
      <circle cx="592" cy="272" r="9"/><circle cx="611" cy="272" r="9"/><circle cx="592" cy="291" r="9"/><circle cx="611" cy="291" r="9"/><path d="M607 272l3 3 5-6"/>
      <!-- interviews -->
      <circle cx="732" cy="305" r="7"/><path d="M720 332c0-9 5-14 12-14"/><path d="M736 332h20l-6-12"/>
      <!-- details -->
      <rect x="836" y="398" width="20" height="24" rx="2"/><line x1="841" y1="405" x2="851" y2="405"/><line x1="841" y1="411" x2="851" y2="411"/><path d="M826 410h-6M866 410h6M846 390v-6M846 430v6"/>
      <!-- immigration -->
      <rect x="884" y="522" width="28" height="36" rx="2"/><line x1="890" y1="532" x2="906" y2="532"/><line x1="890" y1="540" x2="906" y2="540"/><line x1="890" y1="548" x2="900" y2="548"/>
    </g>
    <text x="600" y="578" text-anchor="middle" font-family="Montserrat, sans-serif" font-weight="700" font-size="34" fill="#555">Adept</text>
    <text x="600" y="616" text-anchor="middle" font-family="Montserrat, sans-serif" font-weight="700" font-size="34" fill="#555">Corvana</text>
  </svg>
  <div class="step r" style="left:30px;width:208px;top:524px">We advertise for a job in Sri Lankan Newspapers and social media</div>
  <div class="step r" style="left:130px;width:165px;top:385px">Collecting applications</div>
  <div class="step r" style="left:200px;width:202px;top:280px">Reviewing the suitable candidates</div>
  <div class="step" style="left:400px;width:400px;top:196px;text-align:center">We shortlist candidates</div>
  <div class="step" style="left:800px;width:160px;top:280px">Organise job interviews</div>
  <div class="step" style="left:907px;width:200px;top:375px">After short listing, we are passing the details onto Australian companies</div>
  <div class="step" style="left:958px;width:210px;top:491px">Immigration lawyers to arrange adequate work permits and immigration procedures.</div>
</section>

<section class="jobs">
  <div class="abs center eyebrow" style="top:2324px">Job Listings</div>
  <div class="abs center title" style="top:2366px">Latest Jobs</div>
  <div class="job-head" style="left:345px">Job title</div>
  <div class="job-head" style="left:733px">Job type</div>
  <div class="job-head" style="left:922px">Location</div>

  <div class="job-row shade" style="top:2492px"><div class="job-logo"></div><div class="job-title">Full Stack Developer</div><div class="job-org">Pacific Growth Partners - Meridian Works</div><div class="job-type">Full Time</div><div class="job-loc"><svg width="10" height="14" viewBox="0 0 10 14"><path d="M5 0a5 5 0 0 1 5 5c0 4-5 9-5 9S0 9 0 5a5 5 0 0 1 5-5z" fill="#3b6aa8"/><circle cx="5" cy="5" r="2" fill="#fff"/></svg> Regional QLD Gladstone<br>&nbsp;&nbsp;&nbsp;&amp; Central QLD</div></div>
  <div class="job-row" style="top:2624px"><div class="job-logo"></div><div class="job-title">Senior Civil Project Enginee</div><div class="job-org">Pacific Growth Partners - Meridian Works</div><div class="job-type">Full Time</div><div class="job-loc"><svg width="10" height="14" viewBox="0 0 10 14"><path d="M5 0a5 5 0 0 1 5 5c0 4-5 9-5 9S0 9 0 5a5 5 0 0 1 5-5z" fill="#3b6aa8"/><circle cx="5" cy="5" r="2" fill="#fff"/></svg> Regional QLD Gladstone<br>&nbsp;&nbsp;&nbsp;&amp; Central QLD</div></div>
  <div class="job-row shade" style="top:2748px"><div class="job-logo"></div><div class="job-title">HR Manager</div><div class="job-org">Pacific Growth Partners - Meridian Works</div><div class="job-type">Full Time</div><div class="job-loc"><svg width="10" height="14" viewBox="0 0 10 14"><path d="M5 0a5 5 0 0 1 5 5c0 4-5 9-5 9S0 9 0 5a5 5 0 0 1 5-5z" fill="#3b6aa8"/><circle cx="5" cy="5" r="2" fill="#fff"/></svg> Regional QLD Gladstone<br>&nbsp;&nbsp;&nbsp;&amp; Central QLD</div></div>
  <div class="job-row" style="top:2876px"><div class="job-logo"></div><div class="job-title">Maintenance Fitter</div><div class="job-org">Pacific Growth Partners - Meridian Works</div><div class="job-type">Full Time</div><div class="job-loc"><svg width="10" height="14" viewBox="0 0 10 14"><path d="M5 0a5 5 0 0 1 5 5c0 4-5 9-5 9S0 9 0 5a5 5 0 0 1 5-5z" fill="#3b6aa8"/><circle cx="5" cy="5" r="2" fill="#fff"/></svg> Regional QLD Gladstone<br>&nbsp;&nbsp;&nbsp;&amp; Central QLD</div></div>

  <div class="btn" style="left:518px;top:3016px;width:166px;height:60px">VIEW MORE</div>
</section>

<section class="join-band">
  <div class="join-photo" role="img" aria-label="Smiling man in glasses working on a laptop"></div>
  <svg class="abs" style="left:0;top:0" width="1200" height="580">
    <polygon points="555,0 675,82 555,150" fill="var(--teal)"/>
    <polygon points="620,470 690,500 648,556" fill="var(--deep)"/>
    <polygon points="960,450 1155,395 1125,470 1040,520" fill="var(--navy)" opacity=".85"/>
    <polygon points="1105,400 1170,465 1110,470" fill="var(--green)"/>
  </svg>
  <div class="abs h-font" style="left:661px;top:110px;color:#fff;font-weight:700;font-size:35px;line-height:46px">Join us at<br>Adept Corvana</div>
  <p class="abs" style="left:661px;top:220px;width:450px;color:#e4ecf6;font-size:16px;line-height:27px">Duis aute irure dolor in reprehenderit in voluptate velit esse cillum dolore eu fugiat nulla pariatur sunt in culpa qui officia deserunt mollit anim id est laborum enim ipsam voluptatem quia volu.</p>
  <div class="btn" style="left:661px;top:368px;width:190px;height:60px">JOIN US NOW</div>
</section>

<section class="posts">
  <div class="abs center eyebrow" style="top:3792px">News &amp; Insights</div>
  <div class="abs center title" style="top:3834px">Latest Post</div>
  <article class="post" style="left:111px">
    <div class="post-img" role="img" aria-label="Hands typing on a keyboard with currency symbols" style="background:linear-gradient(135deg,#3d6f9e,#1e3f66)"></div>
    <h3>Managed Solutions &amp; 2022 Salary Guide</h3>
    <div class="by"><svg width="11" height="12" viewBox="0 0 11 12"><circle cx="5.5" cy="3.5" r="3" fill="#3b6aa8"/><path d="M0 12c0-4 2.5-5 5.5-5s5.5 1 5.5 5z" fill="#3b6aa8"/></svg>Admin</div>
    <p>Duis aute irure dolor in reprehenderit in voluptate velit esse cillum dolore eu fugiat nulla pariatur.</p>
  </article>
  <article class="post" style="left:445px">
    <div class="post-img" role="img" aria-label="City skyline at dusk beside a river" style="background:linear-gradient(#7c9cc4 0%,#c9a98a 55%,#4c4a4e 100%)"></div>
    <h3>One of Australia's Best Workplaces 2022</h3>
    <div class="by"><svg width="11" height="12" viewBox="0 0 11 12"><circle cx="5.5" cy="3.5" r="3" fill="#3b6aa8"/><path d="M0 12c0-4 2.5-5 5.5-5s5.5 1 5.5 5z" fill="#3b6aa8"/></svg>Admin</div>
    <p>Duis aute irure dolor in reprehenderit in voluptate velit esse cillum dolore eu fugiat nulla pariatur.</p>
  </article>
  <article class="post" style="left:782px">
    <div class="post-img" role="img" aria-label="Hand holding a passport" style="background:linear-gradient(135deg,#b9bcc2,#27407a 70%,#1d2f5e)"></div>
    <h3>Updates On Australia's Visa &amp; Immigration - August 2022</h3>
    <div class="by"><svg width="11" height="12" viewBox="0 0 11 12"><circle cx="5.5" cy="3.5" r="3" fill="#3b6aa8"/><path d="M0 12c0-4 2.5-5 5.5-5s5.5 1 5.5 5z" fill="#3b6aa8"/></svg>Admin</div>
    <p>Duis aute irure dolor in reprehenderit in voluptate velit esse cillum dolore eu fugiat nulla pariatur.</p>
  </article>
</section>

<footer class="site-footer">
  <div class="brand" style="left:111px;top:80px;color:#fff;font-size:44px;line-height:52px">Adept<br>Corvana</div>
  <div class="foot-col" style="left:488px"><h4>Quick Links</h4><ul><li>Home</li><li>About Us</li><li>Job Seekers</li><li>Employer</li><li>News &amp; Insights</li><li>Contact Us</li></ul></div>
  <div class="foot-col" style="left:677px"><h4>Recruitment</h4><ul><li>Login</li><li>Register</li><li>Submit Resume</li><li>Submit Vacancy</li></ul></div>
  <div class="foot-col" style="left:873px;width:240px"><h4>Contact Us</h4>
    <div style="display:flex;gap:10px;font-size:16px;line-height:25px"><svg width="10" height="14" viewBox="0 0 10 14" style="margin-top:5px"><path d="M5 0a5 5 0 0 1 5 5c0 4-5 9-5 9S0 9 0 5a5 5 0 0 1 5-5z" fill="#fff"/><circle cx="5" cy="5" r="2" fill="#5b5b5c"/></svg><span>412 Harbour Lane, Brisbane<br>Australia 4000</span></div>
    <div style="display:flex;gap:10px;font-size:16px;margin-top:22px;align-items:center"><svg width="12" height="12" viewBox="0 0 12 12"><path d="M2 0l3 3-1.5 2a8 8 0 0 0 3.5 3.5L9 7l3 3-2 2C5 12 0 7 0 2z" fill="#fff"/></svg>1 800 555 0142</div>
    <div style="display:flex;gap:10px;font-size:16px;margin-top:28px;align-items:center"><svg width="14" height="10" viewBox="0 0 14 10"><rect width="14" height="10" fill="#fff"/><path d="M0 0l7 6 7-6" fill="none" stroke="#5b5b5c" stroke-width="1.3"/></svg>info@adeptcorvana.com</div>
  </div>
  <div class="abs" style="left:111px;top:333px;font-size:15px">Copyright © 2022 Adept Corvana - all rights reserved.</div>
</footer>
<div class="social" style="left:941px"></div>
<div class="social" style="left:993px"></div>
<div class="social" style="left:1047px"></div>

</body>
</html>
```